Brenton Civil

We need a Standard Professional Company Letterhead, company standard document template, coversheet template for a civil construction company. We would like the designs to use the company colour red

I have attached existing templates that need to improve greatly but please use as a quide of general layout.

```html
<!DOCTYPE html>
<html lang="en">
<head>
<meta charset="utf-8">
<title>Brenton Civil Letterhead</title>
<link href="https://fonts.googleapis.com/css2?family=Source+Sans+3:wght@400;700&display=swap" rel="stylesheet">
<style>
  :root {
    --brand-red: #b81f2c;
    --brand-red-dark: #9c1a1f;
    --text-grey: #6b6b6b;
    --rule-grey: #d4d4d4;
    --paper: #ffffff;
  }
  html, body {
    margin: 0;
    padding: 0;
    width: 900px;
    height: 1200px;
    overflow: hidden;
    background: var(--paper);
  }
  .letterhead {
    position: relative;
    width: 900px;
    height: 1200px;
    background: var(--paper);
    font-family: "Source Sans 3", "Myriad Pro", Arial, sans-serif;
  }
  .accent-bar-top {
    position: absolute;
    left: 45px;
    top: 0;
    width: 22px;
    height: 78px;
    background: linear-gradient(90deg, #c81e28 0%, var(--brand-red-dark) 60%, #d8323a 100%);
  }
  .accent-bar-side {
    position: absolute;
    left: 45px;
    top: 203px;
    width: 22px;
    bottom: 0;
    background: linear-gradient(90deg, #8d8d8d 0%, #bdbdbd 55%, #e6e6e6 100%);
  }
  .brand {
    position: absolute;
    left: 60px;
    top: 85px;
    display: flex;
    align-items: center;
    gap: 22px;
  }
  .brand-mark {
    width: 104px;
    height: 104px;
    border-radius: 50%;
    background: var(--brand-red);
  }
  .brand-name {
    color: var(--brand-red);
    font-weight: 400;
    font-size: 30px;
    line-height: 1.05;
    letter-spacing: 0.5px;
    text-transform: uppercase;
  }
  .brand-name span { display: block; font-size: 24px; }
  .contact-list {
    position: absolute;
    left: 632px;
    top: 76px;
    margin: 0;
    padding: 0 0 0 12px;
    list-style: none;
    border-left: 1px solid var(--rule-grey);
  }
  .contact-item {
    display: flex;
    align-items: center;
    gap: 6px;
    height: 24.5px;
    font-size: 12.5px;
    color: var(--text-grey);
  }
  .contact-item.address {
    color: var(--brand-red-dark);
    font-weight: 700;
  }
  .contact-icon { width: 14px; height: 14px; flex: none; }
</style>
</head>
<body>
<main class="letterhead">
  <div class="accent-bar-top"></div>
  <div class="accent-bar-side"></div>

  <header class="brand">
    <div class="brand-mark"></div>
    <div class="brand-name">Brenton<span>Civil Pty Ltd</span></div>
  </header>

  <ul class="contact-list">
    <li class="contact-item address">
      <svg class="contact-icon" viewBox="0 0 14 14"><circle cx="7" cy="7" r="6.3" fill="none" stroke="#b81f2c" stroke-width="1.2"/><path d="M7 3.2a2.4 2.4 0 0 0-2.4 2.4C4.6 7.4 7 10.6 7 10.6s2.4-3.2 2.4-5A2.4 2.4 0 0 0 7 3.2z" fill="#b81f2c"/><circle cx="7" cy="5.6" r="0.9" fill="#fff"/></svg>
      PO Box 215, Redgum Flat Qld 4790
    </li>
    <li class="contact-item">
      <svg class="contact-icon" viewBox="0 0 14 14"><circle cx="7" cy="7" r="6.3" fill="none" stroke="#b81f2c" stroke-width="1.2"/><path d="M4.6 3.8l1.3-.3.8 1.7-.8.7c.4.9 1.1 1.6 2 2l.7-.8 1.7.8-.3 1.3c-2.9.3-5.7-2.5-5.4-5.4z" fill="#b81f2c"/></svg>
      0412 555 301
    </li>
    <li class="contact-item">
      <svg class="contact-icon" viewBox="0 0 14 14"><circle cx="7" cy="7" r="6.3" fill="none" stroke="#b81f2c" stroke-width="1.2"/><rect x="3.8" y="4.8" width="6.4" height="4.4" fill="#b81f2c"/><path d="M3.8 4.8L7 7.3l3.2-2.5" fill="none" stroke="#fff" stroke-width="0.7"/></svg>
      info@Brentoncivil.com.au
    </li>
    <li class="contact-item">
      <svg class="contact-icon" viewBox="0 0 14 14"><circle cx="7" cy="7" r="6.3" fill="none" stroke="#b81f2c" stroke-width="1.2"/><circle cx="7" cy="7" r="3.6" fill="none" stroke="#b81f2c" stroke-width="0.8"/><ellipse cx="7" cy="7" rx="1.6" ry="3.6" fill="none" stroke="#b81f2c" stroke-width="0.8"/><path d="M3.4 7h7.2" stroke="#b81f2c" stroke-width="0.8"/></svg>
      Brentoncivil.com.au
    </li>
    <li class="contact-item">
      <svg class="contact-icon" viewBox="0 0 14 14"><circle cx="7" cy="7" r="6.3" fill="none" stroke="#b81f2c" stroke-width="1.2"/><circle cx="7" cy="7" r="4" fill="#9c1a1f"/></svg>
      ABN 12 345 678 901
    </li>
  </ul>
</main>
</body>
</html>
```